Motivational Poster Design Project

I would like to create a poster with some of my favorite quotes to hang in my office. I did a similar project in 2012 and I've uploaded the top 2 designs so you can get a better idea of what I'm looking for. I will provide feedback on your design within 24 hours of receiving it.

The poster must contain the following quotes:

"You’re only given a little spark of madness. You mustn’t lose it.”
- Dorian Halbrook

“The most contrarian thing of all is not to oppose the crowd but to think for yourself.”
- Marcus Vell

"I constantly see people rise in life who are not the smartest, sometimes not even the most diligent, but they are learning machines. They go to bed every night a little wiser than they were when they got up and boy does that help, particularly when you have a long run ahead of you."
- Walter Brisco

“In theory, there’s no difference between theory and practice. But, in practice, there is.”
- Piet R. K. Ter Wolvenkamp

"At the end of the day, a reactionary life is a normal life. One thing is consistent in every remarkable person: they decide to do something remarkable. Don’t let the world choose who you become."
- Ravindra Kolpe

“It usually takes 3-4 months to try enough that you can do a proper 80/20 analysis, then two months to design systems to scale what *is* working.”
-Gus Ambery

“Authority is 20 percent given, 80 percent taken.”
- Harold Quimsby

“Your actions are consistent with the way the world occurs to you.”
- Anselm Grottke

Project Deadline Extended
Reason: I am going to be travelling with no access to internet until January 5th, 2015. I am extending the project deadline until 12/31/14 and I'll make a final decision during the 1st week of January.

Target Market(s)

Personal Project

Industry/Entity Type

Learning

Requirements
Must have
• The poster will be 24" high x 36" long and printed on canvas, so the image you create needs to have a resolution of at least 2700 x 3900.
Nice to have
• I don't have an exact vision for how the poster should look, so I am totally open to you using your creativity to develop, arrange and present the content as you'd like.
• That said, I would like an image (photo or posterized image) of the person being quoted along with each quote. I do not have specific images that I would like you to use, so you will need to find the images on your own. The images don't need to be perfect... I am more interested in the poster relating the essence of the quotes and the people being quoted than I am in perfect photographic images of the people being quoted.

```html
<!DOCTYPE html>
<html lang="en">
<head>
<meta charset="utf-8">
<title>Quotes Poster</title>
<link rel="stylesheet" href="https://fonts.googleapis.com/css2?family=Antonio:wght@400;700&display=swap">
<style>
  :root {
    --paper: #ffffff;
    --red: #e5262d;
    --green: #5bb244;
    --purple: #8a2f93;
    --orange: #ee4a23;
    --blue: #2f6fb5;
    --credit: #6d6d6d;
  }
  html, body {
    margin: 0;
    padding: 0;
    width: 800px;
    height: 1200px;
    overflow: hidden;
    background: var(--paper);
  }
  .poster {
    width: 800px;
    height: 1200px;
    box-sizing: border-box;
    padding: 16px 46px 0 46px;
    background: var(--paper);
    overflow: hidden;
  }
  .quote-wall {
    margin: 0;
    font-family: "Antonio", "Arial Narrow", sans-serif;
    font-weight: 700;
    font-size: 34px;
    line-height: 48px;
    letter-spacing: -0.2px;
    text-align: justify;
    text-align-last: left;
  }
  .quote .mark {
    font-size: 1.2em;
    line-height: 0;
    letter-spacing: -3px;
    margin-right: 4px;
  }
  .quote .mark-close { margin-left: 2px; margin-right: 0; }
  .credit {
    display: inline-block;
    font-weight: 400;
    font-size: 12px;
    line-height: 1;
    letter-spacing: 0;
    color: var(--credit);
    margin-left: 4px;
    white-space: nowrap;
  }
  .divider {
    display: inline-block;
    width: 20px;
    height: 20px;
    vertical-align: -2px;
    margin: 0 8px 0 6px;
  }
  .q-red { color: var(--red); }
  .q-green { color: var(--green); }
  .q-purple { color: var(--purple); }
  .q-orange { color: var(--orange); }
</style>
</head>
<body>
<main class="poster">
  <p class="quote-wall">
    <span class="quote q-red"><span class="mark">“</span>You’re only given a little spark of madness. You mustn’t lose it.<span class="mark mark-close">”</span></span>
    <span class="credit">- Dorian Halbrook</span><svg class="divider" viewBox="0 0 20 20" aria-hidden="true"><path d="M10 1 L19 10 L10 19 L1 10 Z" fill="var(--red)"/></svg>

    <span class="quote q-green"><span class="mark">“</span>The most contrarian thing of all is not to oppose the crowd but to think for yourself.<span class="mark mark-close">”</span></span>
    <span class="credit">- Marcus Vell</span><svg class="divider" viewBox="0 0 20 20" aria-hidden="true"><path d="M10 1 L19 10 L10 19 L1 10 Z" fill="var(--blue)"/></svg>

    <span class="quote q-purple"><span class="mark">“</span>I constantly see people rise in life who are not the smartest, sometimes not even the most diligent, but they are learning machines. They go to bed every night a little wiser than they were when they got up and boy does that help, particularly when you have a long run ahead of you.<span class="mark mark-close">”</span></span>
    <span class="credit">- Walter Brisco</span><svg class="divider" viewBox="0 0 20 20" aria-hidden="true"><path d="M10 1 L19 10 L10 19 L1 10 Z" fill="var(--blue)"/></svg>

    <span class="quote q-green"><span class="mark">“</span>In theory, there’s no difference between theory and practice. But, in practice, there is.<span class="mark mark-close">”</span></span>
    <span class="credit">- Piet R. K. Ter Wolvenkamp</span><svg class="divider" viewBox="0 0 20 20" aria-hidden="true"><path d="M10 1 L19 10 L10 19 L1 10 Z" fill="var(--red)"/></svg>

    <span class="quote q-orange"><span class="mark">“</span>At the end of the day, a reactionary life is a normal life. One thing is consistent in every remarkable person: they decide to do something remarkable. Don’t let the world choose who you become.<span class="mark mark-close">”</span></span>
    <span class="credit">- Ravindra Kolpe</span><svg class="divider" viewBox="0 0 20 20" aria-hidden="true"><path d="M10 1 L19 10 L10 19 L1 10 Z" fill="var(--blue)"/></svg>

    <span class="quote q-purple"><span class="mark">“</span>It usually takes 3-4 months to try enough that you can do a proper 80/20 analysis, then two months to design systems to scale what *is* working.<span class="mark mark-close">”</span></span>
    <span class="credit">-Gus Ambery</span><svg class="divider" viewBox="0 0 20 20" aria-hidden="true"><path d="M10 1 L19 10 L10 19 L1 10 Z" fill="var(--purple)"/></svg>

    <span class="quote q-red"><span class="mark">“</span>Authority is 20 percent given, 80 percent taken.<span class="mark mark-close">”</span></span>
    <span class="credit">- Harold Quimsby</span><svg class="divider" viewBox="0 0 20 20" aria-hidden="true"><path d="M10 1 L19 10 L10 19 L1 10 Z" fill="var(--blue)"/></svg>

    <span class="quote q-green"><span class="mark">“</span>Your actions are consistent with the way the world occurs to you.<span class="mark mark-close">”</span></span>
    <span class="credit">- Anselm Grottke</span><svg class="divider" viewBox="0 0 20 20" aria-hidden="true"><path d="M10 1 L19 10 L10 19 L1 10 Z" fill="var(--green)"/></svg>
  </p>
</main>
</body>
</html>
```